Corvale Real Estate

I manage 2 firms. The first one is Felmont and the logo is in blue (see the file) but i need a design for my business card for the second firm called CORVALE IMMOBILIER. This one is in charge of Real estate developer.

Colors
3176b5

```html
<!DOCTYPE html>
<html lang="fr">
<head>
<meta charset="utf-8">
<title>Corvale Immobilier — Business Card</title>
<link rel="stylesheet" href="https://fonts.googleapis.com/css2?family=Montserrat:wght@400;500&display=swap">
<style>
  :root {
    --card-bg: #a3cfe7;
    --card-shade: #97c6e1;
    --ink: #17578a;
    --brand: #2d8fd9;
  }
  * { margin: 0; padding: 0; box-sizing: border-box; }
  html, body {
    width: 1200px;
    height: 686px;
    overflow: hidden;
    background: var(--card-bg);
  }
  .business-card {
    position: relative;
    width: 1200px;
    height: 686px;
    background: var(--card-bg);
    font-family: "Montserrat", Arial, sans-serif;
    color: var(--ink);
    overflow: hidden;
  }
  .backdrop-shape {
    position: absolute;
    left: 0;
    top: 0;
  }
  .holder-name {
    position: absolute;
    left: 88px;
    top: 80px;
    font-size: 69px;
    font-weight: 400;
    letter-spacing: 0.5px;
    line-height: 1;
    white-space: nowrap;
  }
  .contact-list {
    position: absolute;
    left: 91px;
    top: 500px;
    list-style: none;
    font-size: 22px;
    font-weight: 500;
    line-height: 1;
    white-space: nowrap;
  }
  .contact-list li { margin-bottom: 20px; }
  .brand-lockup {
    position: absolute;
    left: 800px;
    top: 532px;
    display: flex;
    align-items: center;
    gap: 16px;
    white-space: nowrap;
  }
  .brand-mark {
    flex: none;
    width: 44px;
    height: 44px;
    background: var(--brand);
  }
  .brand-name {
    font-size: 20px;
    font-weight: 500;
    letter-spacing: 2px;
    line-height: 1;
    color: var(--brand);
  }
</style>
</head>
<body>
  <main class="business-card">
    <svg class="backdrop-shape" width="620" height="686" viewBox="0 0 620 686" aria-hidden="true">
      <rect x="0" y="0" width="616" height="686" fill="var(--card-shade)" opacity="0.4"/>
    </svg>

    <h1 class="holder-name">Elias Marrow</h1>

    <ul class="contact-list">
      <li class="contact-email">elias@corvale-immo.fr</li>
      <li class="contact-web">www.corvale-immo.fr</li>
      <li class="contact-phone">+33 1 47 22 18 64</li>
    </ul>

    <div class="brand-lockup">
      <span class="brand-mark"></span>
      <span class="brand-name">CORVALE IMMOBILIER</span>
    </div>
  </main>
</body>
</html>
```